Business Card Design Project For Moving Company

Hello,

We need the business card to be 2 sided and we were thinking to use the logo on the front of the card (see file 1 attached) and the text "logo" (see file 2 attached) in the back of the card. We're looking for a powerful design that will help us build our brand, as our company is new.
We are a full service moving company (no storage) located in San Diego, CA, USA. The design should communicate to our potential customers that we have the highest level of service, customer satisfaction is our number one goal, our team is professional and efficient.

Thank you,

Dorn
Updates

Project Deadline Extended
Reason: We would like to have more time to provide feedback for the designs already submitted. Thank you, Dorn

Industry/Entity Type

Moving Company

Requirements
Must have
• Front of the card must have the following text and logo:
Haulbright, Inc
Residential And Commercial
Local And Long Distance
Address: 7312 Quillmont Rd, #146,
San Diego, CA, 92784
P: 855-372-LIFT (5438)
F: 858-529-4407
info@haul-bright.com
www.haul-bright.com

Back of the card must have the following text and text "logo" (file 2 attached):

The best compliment we can ever receive is a referral from our clients.

```html
<!DOCTYPE html>
<html lang="en">
<head>
<meta charset="utf-8">
<title>Haulbright, Inc – Business Card</title>
<link rel="stylesheet" href="https://fonts.googleapis.com/css2?family=Open+Sans:wght@400;600;700&display=swap">
<style>
  :root {
    --stage: #2c2c2c;
    --card-light: #f4f4f4;
    --card-light-edge: #d9d9d9;
    --card-dark: #3b3b3b;
    --card-dark-band: #444444;
    --brand-red: #d3161b;
    --ink: #2a2a2a;
    --ink-soft: #7a7a7a;
    --white: #ffffff;
    --white-soft: #cfcfcf;
  }
  * { box-sizing: border-box; margin: 0; padding: 0; }
  html, body {
    width: 1200px; height: 800px; overflow: hidden;
    background: var(--stage);
    font-family: "Open Sans", Arial, sans-serif;
  }
  .canvas { position: relative; width: 1200px; height: 800px; }

  /* Front card */
  .card-front {
    position: absolute; left: 30px; top: 40px;
    width: 700px; height: 380px;
    background: radial-gradient(ellipse at 52% 32%, var(--white) 0%, var(--card-light) 45%, var(--card-light-edge) 100%);
    box-shadow: 0 6px 0 #1a1a1a;
  }
  .brand {
    position: absolute; left: 34px; top: 62px;
    font-weight: 700; font-size: 54px; line-height: 1;
    letter-spacing: -1px; color: var(--ink);
  }
  .brand-tagline {
    position: absolute; left: 150px; top: 124px;
    width: 236px; text-align: right;
    font-size: 15px; line-height: 20px; color: var(--ink-soft);
    text-transform: uppercase;
  }
  .owner { position: absolute; left: 150px; top: 306px; }
  .owner-name { font-size: 23px; color: var(--ink); line-height: 1.1; }
  .owner-role { font-size: 13px; color: var(--brand-red); margin-top: 2px; padding-left: 27px; }

  .contact-list { position: absolute; left: 468px; top: 78px; list-style: none; }
  .contact-item {
    display: flex; align-items: center; gap: 8px;
    font-size: 14.5px; color: var(--ink); line-height: 19px;
  }
  .contact-item.address { align-items: flex-start; margin-bottom: 72px; }
  .contact-item + .contact-item { margin-top: 12px; }
  .contact-item.address + .contact-item { margin-top: 0; }
  .contact-icon {
    flex: none; width: 24px; height: 26px;
    background: var(--brand-red); border-radius: 2px;
    display: flex; align-items: center; justify-content: center;
  }
  .contact-icon.large { width: 28px; height: 32px; margin-top: 2px; }
  .contact-icon svg { width: 16px; height: 16px; }

  /* Back card */
  .card-back {
    position: absolute; left: 540px; top: 432px;
    width: 620px; height: 344px;
    background: var(--card-dark); overflow: hidden;
  }
  .back-band {
    position: absolute; right: 40px; top: 0;
    width: 170px; height: 100%;
    background: var(--card-dark-band);
  }
  .back-lockup {
    position: absolute; left: 210px; top: 96px;
    display: flex; flex-direction: column; align-items: flex-start;
  }
  .back-mark-row { display: flex; align-items: center; gap: 12px; }
  .back-dot { width: 26px; height: 26px; border-radius: 50%; background: var(--white); }
  .back-name { font-weight: 700; font-size: 40px; color: var(--white); line-height: 1; }
  .back-tagline {
    margin-top: 14px; font-size: 11px; line-height: 14px; color: var(--white);
  }
  .back-quote {
    position: absolute; left: 40px; bottom: 32px;
    width: 320px;
    font-size: 12px; line-height: 17px; font-style: normal;
    color: var(--white-soft);
  }
</style>
</head>
<body>
<main class="canvas">

  <section class="card-front" aria-label="Business card front">
    <h1 class="brand">HAULBRIGHT</h1>
    <p class="brand-tagline">Residential and Commercial<br>Local and Long Distance</p>

    <div class="owner">
      <p class="owner-name">OWNER NAME</p>
      <p class="owner-role">General Manager</p>
    </div>

    <ul class="contact-list">
      <li class="contact-item address">
        <span class="contact-icon large">
          <svg viewBox="0 0 16 16"><path d="M8 1a5 5 0 0 0-5 5c0 3.6 5 9 5 9s5-5.4 5-9a5 5 0 0 0-5-5zm0 7a2 2 0 1 1 0-4 2 2 0 0 1 0 4z" fill="#fff"/></svg>
        </span>
        <span>7312 Quillmont Rd, #146,<br>San Diego, CA, 92784</span>
      </li>
      <li class="contact-item">
        <span class="contact-icon">
          <svg viewBox="0 0 16 16"><rect x="4" y="1" width="8" height="14" rx="1.5" fill="#fff"/><rect x="5.5" y="3" width="5" height="5" fill="#d3161b"/><rect x="5.5" y="9.5" width="5" height="4" fill="#d3161b" opacity=".5"/></svg>
        </span>
        <span>855-372-LIFT (5438)</span>
      </li>
      <li class="contact-item">
        <span class="contact-icon">
          <svg viewBox="0 0 16 16"><rect x="4" y="1.5" width="8" height="4" fill="#fff"/><rect x="1.5" y="5.5" width="13" height="6" rx="1" fill="#fff"/><rect x="4" y="9.5" width="8" height="5" fill="#fff" stroke="#d3161b" stroke-width="1"/></svg>
        </span>
        <span>858-529-4407</span>
      </li>
      <li class="contact-item">
        <span class="contact-icon">
          <svg viewBox="0 0 16 16"><rect x="1.5" y="3.5" width="13" height="9" fill="#fff"/><path d="M1.5 3.5 8 9l6.5-5.5" fill="none" stroke="#d3161b" stroke-width="1.2"/></svg>
        </span>
        <span>info@haul-bright.com</span>
      </li>
      <li class="contact-item">
        <span class="contact-icon">
          <svg viewBox="0 0 16 16" fill="none" stroke="#fff" stroke-width="1.2"><circle cx="8" cy="8" r="6.3"/><ellipse cx="8" cy="8" rx="2.8" ry="6.3"/><path d="M1.7 8h12.6M2.8 4.8h10.4M2.8 11.2h10.4"/></svg>
        </span>
        <span>www.haul-bright.com</span>
      </li>
    </ul>
  </section>

  <section class="card-back" aria-label="Business card back">
    <div class="back-band"></div>
    <div class="back-lockup">
      <div class="back-mark-row">
        <span class="back-dot"></span>
        <span class="back-name">Haulbright</span>
      </div>
      <p class="back-tagline">Residential And Commercial<br>Local And Long Distance</p>
    </div>
    <blockquote class="back-quote">The best compliment we can ever receive is a referral from our clients.</blockquote>
  </section>

</main>
</body>
</html>
```